industrial tools need a business card design

Brantor Tools including Cable Tools, Pipe Tools, Rebar Tools, Hydraulic Tools Packing Machine, We need design a business card, Design business card needs to accord with company logo and color, please refer to our website products at the same time:www.brantor-example.com, please see our logo(CDR)in attach,we need cdr type,thanks!

Industry/Entity Type

Industrial

```html
<!DOCTYPE html>
<html lang="en">
<head>
<meta charset="utf-8">
<title>Brantor Tools – Stationery</title>
<link href="https://fonts.googleapis.com/css2?family=Open+Sans:wght@400;600;800&display=swap" rel="stylesheet">
<style>
  :root {
    --canvas: #d6d6d6;
    --paper: #f2f1f0;
    --ink: #2b2623;
    --ink-soft: #5a5552;
    --brand-dark: #3a322e;
    --brand-orange: #e0601c;
    --band-green: #1f2a1e;
    --swoosh-grey: #dcdad8;
    --band-grey: #55575a;
  }
  * { box-sizing: border-box; margin: 0; padding: 0; }
  html, body { width: 1200px; height: 900px; overflow: hidden; }
  body {
    background: var(--canvas);
    font-family: "Open Sans", Arial, sans-serif;
    color: var(--ink);
    position: relative;
  }
  .wordmark {
    display: inline-flex; align-items: center; gap: 6px;
    font-weight: 800; letter-spacing: 1px; color: var(--ink);
  }
  .wordmark__dot { width: 8px; height: 8px; background: var(--brand-orange); }

  /* Letterhead */
  .letterhead {
    position: absolute; left: 60px; top: 60px; width: 560px; height: 780px;
    background: var(--paper); overflow: hidden;
  }
  .letterhead .wordmark { position: absolute; left: 56px; top: 50px; font-size: 24px; }
  .letter-body {
    position: absolute; left: 120px; top: 118px; width: 380px;
    font-size: 11px; line-height: 18px; color: var(--ink-soft);
  }
  .letter-body p { margin-bottom: 8px; }
  .letter-body strong { color: var(--ink); font-weight: 600; }
  .letter-body .indent { padding-left: 16px; }
  .signature {
    width: 110px; height: 34px; margin-top: 6px;
    background: #e4e2e0; border-radius: 3px;
  }
  .letterhead__decor {
    position: absolute; right: -40px; bottom: 40px; width: 420px; height: 260px;
    background: radial-gradient(ellipse at 70% 60%, var(--swoosh-grey), transparent 70%);
  }
  .letterhead__band {
    position: absolute; left: 0; right: 0; bottom: 50px; height: 9px; display: flex;
  }
  .letterhead__band-dark { flex: 2; background: var(--band-green); }
  .letterhead__band-orange { flex: 1; background: var(--brand-orange); margin-left: 4px; }

  /* Phone screen */
  .phone-screen {
    position: absolute; left: 825px; top: 60px; width: 170px; height: 270px;
    background: #fafafa; overflow: hidden; border: 1px solid #c8c8c8;
  }
  .phone-screen .wordmark { position: absolute; left: 18px; top: 34px; font-size: 18px; }
  .phone-screen__decor {
    position: absolute; left: 0; right: 0; bottom: 0; height: 170px;
    background: linear-gradient(170deg, #f5ece8 0%, #d9d8d7 55%, #c9c9c9 100%);
  }

  /* Business cards */
  .card { position: absolute; left: 700px; width: 420px; height: 240px; overflow: hidden; }
  .card--back { top: 360px; background: var(--brand-dark); }
  .card--back svg { position: absolute; left: 0; top: 0; }
  .card--back .wordmark {
    position: absolute; right: 40px; bottom: 56px; font-size: 34px; color: #fff;
  }
  .card--front { top: 620px; background: var(--paper); }
  .card--front .wordmark { position: absolute; left: 28px; top: 26px; font-size: 26px; }
  .card__decor {
    position: absolute; right: -30px; top: 60px; width: 300px; height: 150px;
    background: radial-gradient(ellipse at 60% 50%, var(--swoosh-grey), transparent 70%);
  }
  .contact { position: absolute; left: 28px; top: 84px; font-size: 10px; line-height: 16px; color: var(--ink-soft); }
  .contact__name { font-size: 13px; font-weight: 600; color: var(--ink); letter-spacing: .5px; }
  .contact__title { color: var(--brand-orange); margin-bottom: 4px; }
  .contact__line { display: flex; align-items: center; gap: 6px; }
  .contact__line::before {
    content: ""; width: 6px; height: 6px; border-radius: 50%; background: var(--brand-orange);
  }
  .contact__address { margin-top: 10px; }
  .social { position: absolute; right: 28px; bottom: 22px; display: flex; gap: 4px; }
  .social span { width: 12px; height: 12px; }
  .social span:nth-child(1) { background: #3b5998; }
  .social span:nth-child(2) { background: #c8312b; }
  .social span:nth-child(3) { background: #39a9e0; }
</style>
</head>
<body>

<section class="letterhead">
  <div class="wordmark"><span>BRANTOR</span><span class="wordmark__dot"></span></div>
  <div class="letter-body">
    <p>28 June 2013<br>[Insert Name and Address of Solicitor]</p>
    <p>Dear Mr/Ms [Solicitor Name]</p>
    <p><strong>[Insert Matter details]</strong></p>
    <p>In this matter [insert details of what happened]<br>[insert who appeared for the Other Party]</p>
    <p>The following Orders were made:<br><span class="indent">1. [Insert Orders that were made]</span></p>
    <p>If I can assist you with anything further please do not hesitate to contact me.<br>I enclose a memorandum of fees for your attention.</p>
    <p>Yours faithfully</p>
    <div class="signature" role="img" aria-label="Handwritten signature"></div>
  </div>
  <div class="letterhead__decor" role="img" aria-label="Faint grey curved brand decoration"></div>
  <div class="letterhead__band">
    <span class="letterhead__band-dark"></span>
    <span class="letterhead__band-orange"></span>
  </div>
</section>

<section class="phone-screen">
  <div class="wordmark"><span>BRANTOR</span><span class="wordmark__dot"></span></div>
  <div class="phone-screen__decor" role="img" aria-label="Soft grey curved brand decoration"></div>
</section>

<section class="card card--back">
  <svg width="420" height="120" viewBox="0 0 420 120" aria-hidden="true">
    <polygon points="0,40 420,0 420,26 0,74" fill="var(--brand-orange)"/>
    <polygon points="0,82 420,34 420,52 0,110" fill="var(--band-grey)"/>
  </svg>
  <div class="wordmark"><span>BRANTOR</span><span class="wordmark__dot"></span></div>
</section>

<section class="card card--front">
  <div class="card__decor" role="img" aria-label="Faint grey curved brand decoration"></div>
  <div class="wordmark"><span>BRANTOR</span><span class="wordmark__dot"></span></div>
  <div class="contact">
    <div class="contact__name">DANIEL ROWE</div>
    <div class="contact__title">Managing Director</div>
    <div class="contact__line">+00-555-0142-880</div>
    <div class="contact__line">info@brantor-example.com</div>
    <div class="contact__line">www.brantor-example.com</div>
    <div class="contact__address">No.42 Harbor Rd, Eastfield</div>
  </div>
  <div class="social" aria-label="Social links"><span></span><span></span><span></span></div>
</section>

</body>
</html>
```